Business Card for Pottery and Jewellery Designer

A new business card design is needed to accompany a newly launching pottery and jewellery website. The company logo has been attached for use. The company is called Glazewick Studio. For a sense of the vibe please see the website (it is currently under construction but this way you'll get a feel for the style) www.GlazewickStudio.com

The website font is Pontano Sans for the body of the text with Overlock for headers.

The overall look should be clean and elegant. The back side can have just the logo. The front side should have a smaller logo and the following details displayed:

Glazewick Studio
Designer: Hollis Marrow
Phone: xxx.xxx.xxxx
Email: Designer@GlazewickStudio.com

The structure of displaying this is completely up to you. Different layouts and creative methods of displaying contact info are welcome as long as it stays clean/uncluttered.

No product photographs are to be included in the design as the catalogue changes quickly.

Colour preferences lean towards elegant and understated (charcoal grey, dark navy blue etc.)

Please let me know if you have any further questions or further details required.

Target Market(s)

Target market is 30+ year old women

Industry/Entity Type

Construction

Colors
ffffff
1b1b1b
474747
d9d9d9
fafafa
0355a3

Requirements
Must have
• The submissions so far have looked very typical and don't stand out right now. They're also all in navy with very little variation. I'm looking for something that stands out a it more while still being clean-looking.
Nice to have
• I've attached a few design samples and an idea for a backdrop. It would be great to see some designs in black, white, and grey with only a hint of color.
Should not have
• Product Images

```html
<!DOCTYPE html>
<html lang="en">
<head>
<meta charset="utf-8">
<title>Glazewick Studio – Business Card</title>
<link href="https://fonts.googleapis.com/css2?family=Overlock:wght@400;700&family=Pontano+Sans&display=swap" rel="stylesheet">
<style>
  :root {
    --backdrop: #4a2a1c;
    --card: #1b1b1b;
    --card-edge: #232323;
    --ink: #fafafa;
    --muted: #474747;
    --accent: #2a9fd6;
  }
  * { box-sizing: border-box; margin: 0; padding: 0; }
  html, body {
    width: 1200px; height: 1181px; overflow: hidden;
    background: var(--backdrop);
  }
  .canvas { position: relative; width: 1200px; height: 1181px; }
  .card {
    position: absolute; left: 209px; width: 781px; height: 451px;
    background: radial-gradient(ellipse at 50% 40%, var(--card-edge), var(--card) 75%);
    box-shadow: 0 6px 14px rgba(0,0,0,.5);
  }
  .card--back { top: 91px; }
  .card--front { top: 630px; }

  .brand {
    position: absolute; left: 160px; top: 202px;
    display: flex; align-items: center; gap: 30px;
  }
  .brand__mark {
    width: 58px; height: 58px; border-radius: 50%;
    background: var(--muted);
  }
  .brand__name {
    font-family: "Overlock", sans-serif; font-weight: 400;
    font-size: 34px; letter-spacing: .5px; color: var(--ink);
    text-transform: uppercase;
  }

  .person {
    position: absolute; left: 0; right: 0; top: 204px; text-align: center;
    font-family: "Overlock", sans-serif; font-size: 36px; color: var(--ink);
  }

  .contact {
    position: absolute; left: 0; right: 0; top: 414px;
    display: flex; justify-content: center; gap: 24px;
    font-family: "Pontano Sans", sans-serif; font-size: 15px; color: var(--ink);
  }
  .contact__item { display: flex; align-items: center; gap: 6px; }
  .contact__icon { width: 17px; height: 17px; }
</style>
</head>
<body>
<main class="canvas">
  <section class="card card--back">
    <div class="brand">
      <span class="brand__mark"></span>
      <span class="brand__name">Glazewick Studio</span>
    </div>
  </section>

  <section class="card card--front">
    <p class="person">Hollis Marrow</p>
    <ul class="contact">
      <li class="contact__item">
        <svg class="contact__icon" viewBox="0 0 20 20" aria-hidden="true">
          <circle cx="10" cy="10" r="9.5" fill="var(--accent)"/>
          <path d="M6.5 5.5l2 0 1 2.5-1.3 1a6 6 0 0 0 2.8 2.8l1-1.3 2.5 1v2a1 1 0 0 1-1 1A8 8 0 0 1 5.5 6.5a1 1 0 0 1 1-1z" fill="var(--card)"/>
        </svg>
        <span>555-014-2287</span>
      </li>
      <li class="contact__item">
        <svg class="contact__icon" viewBox="0 0 20 20" aria-hidden="true">
          <circle cx="10" cy="10" r="9.5" fill="var(--accent)"/>
          <text x="10" y="14" text-anchor="middle" font-family="Arial, sans-serif" font-size="12" fill="var(--card)">@</text>
        </svg>
        <span>Designer@GlazewickStudio.com</span>
      </li>
      <li class="contact__item">
        <svg class="contact__icon" viewBox="0 0 20 20" aria-hidden="true">
          <circle cx="10" cy="10" r="9.5" fill="var(--accent)"/>
          <g fill="none" stroke="var(--card)" stroke-width="1.2">
            <circle cx="10" cy="10" r="5.5"/>
            <ellipse cx="10" cy="10" rx="2.3" ry="5.5"/>
            <line x1="4.5" y1="10" x2="15.5" y2="10"/>
          </g>
        </svg>
        <span>GlazewickStudio.com</span>
      </li>
    </ul>
  </section>
</main>
</body>
</html>
```